ORVA TELMINO - LUXURY RESORT CORVANE HOTEL

We wanna promote the luxury hotel based on marroquian stylish luxury decor, it is still a project but we need to expose it.
Houses will be A frame type houses surrounded by florest and water dumps - please check - odeleite amber heron at google to check localisation
Container luxury houses also will be included heaven blue velvet and green and rose gold are the Color. The sky is the limit.

```html
<!DOCTYPE html>
<html lang="en">
<head>
<meta charset="utf-8">
<title>Orva Telmino – Business Card</title>
<link href="https://fonts.googleapis.com/css2?family=Cinzel:wght@400&family=Poppins:wght@400;600;700&display=swap" rel="stylesheet">
<style>
  :root {
    --page: #ececec;
    --paper: #f4f3f3;
    --forest: #12251b;
    --gold: #c49a62;
    --ink: #2b2b2b;
    --muted: #4a4a4a;
  }
  html, body { margin: 0; padding: 0; overflow: hidden; }
  body { width: 1200px; height: 1020px; background: var(--page); position: relative; font-family: "Poppins", sans-serif; }

  .card { position: absolute; width: 660px; height: 380px; left: 270px; box-shadow: 0 14px 30px rgba(0,0,0,.28); overflow: hidden; }
  .card--front { top: 70px; background: var(--paper); }
  .card--back { top: 540px; background: var(--forest); }

  /* front */
  .side-strip { position: absolute; right: 0; top: 0; width: 88px; height: 100%; background: var(--forest); }
  .side-strip__text { position: absolute; left: 50%; top: 50%; transform: translate(-50%, -50%) rotate(90deg); white-space: nowrap;
    font-family: "Cinzel", serif; font-size: 15px; letter-spacing: 2px; color: var(--gold); }
  .rule-bold { position: absolute; left: 0; top: 126px; width: 300px; height: 10px; background: var(--forest); }
  .rule-thin { position: absolute; left: 300px; top: 126px; width: 272px; height: 2px; background: var(--forest); }

  .holder { position: absolute; left: 38px; top: 66px; }
  .holder__name { margin: 0; font-weight: 700; font-size: 29px; color: #555; line-height: 1.1; letter-spacing: -.3px; }
  .holder__role { margin: 2px 0 0 14px; font-weight: 700; font-size: 13px; color: #111; }

  .contacts { position: absolute; left: 52px; top: 168px; margin: 0; padding: 0; list-style: none; }
  .contacts li { display: flex; align-items: center; gap: 12px; height: 29px; font-size: 14px; color: var(--muted); }
  .contacts svg { width: 22px; height: 22px; flex: none; }

  .brand { font-family: "Cinzel", serif; font-weight: 400; color: var(--gold); letter-spacing: 4px; white-space: nowrap; }
  .brand--front { position: absolute; left: 120px; top: 305px; font-size: 28px; }

  /* back */
  .brand-lockup { position: absolute; left: 0; right: 0; top: 150px; text-align: center; }
  .brand--back { font-size: 40px; }
  .brand-lockup__tagline { margin-top: 6px; font-family: "Cinzel", serif; font-size: 15px; letter-spacing: 2.5px; color: #b8ab96; }
  .edge-tab { position: absolute; width: 10px; height: 44px; background: var(--gold); }
  .edge-tab--left { left: 0; top: 250px; }
  .edge-tab--right { right: 0; top: 80px; }
</style>
</head>
<body>

<section class="card card--front" aria-label="Business card front">
  <div class="side-strip"><span class="side-strip__text">LUXURY RESORT CORVANE HOTEL</span></div>

  <div class="holder">
    <h1 class="holder__name">Nadira Elkoury</h1>
    <p class="holder__role">Founder &amp; Head of Design</p>
  </div>

  <div class="rule-bold"></div>
  <div class="rule-thin"></div>

  <ul class="contacts">
    <li>
      <svg viewBox="0 0 22 22" aria-hidden="true"><circle cx="11" cy="11" r="11" fill="#12251b"/>
        <path d="M7.5 6.5l2 0 .8 2.6-1.2 1a6 6 0 0 0 2.8 2.8l1-1.2 2.6.8v2c0 .6-.5 1-1 1A8.5 8.5 0 0 1 6.5 7.5c0-.5.4-1 1-1z" fill="#fff"/></svg>
      +20 5550 0142
    </li>
    <li>
      <svg viewBox="0 0 22 22" aria-hidden="true"><circle cx="11" cy="11" r="11" fill="#12251b"/>
        <circle cx="11" cy="11" r="5" fill="none" stroke="#fff" stroke-width="1.2"/>
        <ellipse cx="11" cy="11" rx="2.2" ry="5" fill="none" stroke="#fff" stroke-width="1"/>
        <line x1="6" y1="11" x2="16" y2="11" stroke="#fff" stroke-width="1"/></svg>
      www.velmaran.com
    </li>
    <li>
      <svg viewBox="0 0 22 22" aria-hidden="true"><circle cx="11" cy="11" r="11" fill="#12251b"/>
        <rect x="6" y="7.5" width="10" height="7" fill="none" stroke="#fff" stroke-width="1.2"/>
        <path d="M6 7.5l5 4 5-4" fill="none" stroke="#fff" stroke-width="1.2"/></svg>
      Nadira.Elkoury@velmaran.com
    </li>
    <li>
      <svg viewBox="0 0 22 22" aria-hidden="true"><circle cx="11" cy="11" r="11" fill="#12251b"/>
        <path d="M11 16.5s-4-4.2-4-7a4 4 0 0 1 8 0c0 2.8-4 7-4 7z" fill="#fff"/>
        <circle cx="11" cy="9.5" r="1.5" fill="#12251b"/></svg>
      Lindor Lane - Sefra District
    </li>
  </ul>

  <div class="brand brand--front">ORVA TELMINO</div>
</section>

<section class="card card--back" aria-label="Business card back">
  <div class="edge-tab edge-tab--left"></div>
  <div class="edge-tab edge-tab--right"></div>
  <div class="brand-lockup">
    <div class="brand brand--back">ORVA TELMINO</div>
    <div class="brand-lockup__tagline">~ LUXURY RESORT CORVANE HOTEL ~</div>
  </div>
</section>

</body>
</html>
```